Name card for fertilizer industry

We 1. produce liquid fertilizer 2. gardening supply 3. Import&Export gardening related product.
I want the name card double-sided(Chinese & English version)
detail has chinese charactor for name and address.
Updates
Target Market(s)
Farmers
Industry/Entity Type
Industry
Contact Information for Business Card
Name: Daniel Lo (陳明達)
TEL: +886-48-516042
FAX:+886-48-590714
MOBILE: +886-912-804-153
ADDRESS: No.58, Baoan Rd, Dapu Township, Kexi County , TAIWAN(R.O.C) 柯溪縣大埔鎮寶安路58號
Look and feel
Each slider illustrates characteristics of the customer's brand and the style your logo design should communicate.

```html
<!DOCTYPE html>
<html lang="en">
<head>
<meta charset="utf-8">
<title>Tian He Agri – Name Card</title>
<link rel="stylesheet" href="https://fonts.googleapis.com/css2?family=Noto+Sans+TC:wght@400;500;700&family=Open+Sans:wght@400;600;700&display=swap">
<style>
  :root {
    --stage: #d5d5d5;
    --leaf-green: #62b846;
    --deep-brown: #2b1510;
    --paper: #ffffff;
    --ink: #231512;
    --photo-field: #7fae55;
    --photo-field-soft: #9cc47a;
    --photo-orchard: #c9a9b4;
    --photo-orchard-soft: #a9b58a;
    --soft-mint: #e3f0dd;
  }
  * { margin: 0; padding: 0; box-sizing: border-box; }
  html, body { width: 1200px; height: 900px; overflow: hidden; }
  body {
    background: var(--stage);
    font-family: "Open Sans", Arial, sans-serif;
    position: relative;
  }
  .card {
    position: absolute;
    top: 290px;
    width: 540px;
    height: 320px;
    border-radius: 24px;
    overflow: hidden;
    background: var(--leaf-green);
  }
  .card--front { left: 40px; }
  .card--back { left: 620px; }
  .card__shapes { position: absolute; inset: 0; }

  /* front */
  .brand-disc {
    position: absolute; left: 52px; top: 92px;
    width: 120px; height: 120px; border-radius: 50%;
    background: var(--soft-mint);
  }
  .brand {
    position: absolute; left: 250px; top: 24px; width: 270px;
  }
  .brand__zh {
    font-family: "Noto Sans TC", sans-serif;
    font-weight: 500; font-size: 38px; letter-spacing: 4px;
    color: var(--ink); line-height: 1.1;
  }
  .brand__en {
    font-size: 12.5px; color: var(--paper); letter-spacing: 0.3px; margin-top: 4px;
  }
  .holder {
    position: absolute; left: 250px; top: 128px; width: 270px;
    text-align: center; color: var(--ink);
  }
  .holder__en { font-weight: 700; font-size: 19px; line-height: 24px; }
  .holder__zh {
    font-family: "Noto Sans TC", sans-serif; font-weight: 500;
    font-size: 14px; letter-spacing: 2px; line-height: 20px;
  }
  .contacts {
    position: absolute; left: 250px; top: 186px;
    list-style: none; color: var(--paper); font-size: 14.5px; line-height: 20px;
  }
  .contacts li { display: flex; align-items: center; gap: 6px; }
  .contacts svg { width: 13px; height: 13px; flex: none; }
  .address {
    position: absolute; left: 250px; top: 272px; width: 275px;
    color: var(--paper); font-size: 9.5px; line-height: 14px;
  }
  .address__zh { font-family: "Noto Sans TC", sans-serif; font-size: 10.5px; }

  /* back */
  .back-disc {
    position: absolute; left: 235px; top: 24px;
    width: 80px; height: 80px; border-radius: 50%;
    background: var(--deep-brown);
  }
  .brand--back { left: 200px; top: 228px; width: 200px; text-align: center; }
  .brand--back .brand__zh { font-size: 30px; letter-spacing: 3px; }
  .brand--back .brand__en { font-size: 10px; margin-top: 2px; }
</style>
</head>
<body>

<section class="card card--front" aria-label="Name card, front">
  <svg class="card__shapes" viewBox="0 0 540 320" aria-hidden="true">
    <path d="M0 0 H215 C250 110 235 240 170 320 H0 Z" fill="var(--paper)"/>
    <path d="M190 0 H250 C262 70 252 140 228 190 C238 120 228 55 190 0 Z" fill="var(--deep-brown)"/>
  </svg>
  <div class="brand-disc"></div>

  <div class="brand">
    <div class="brand__zh">田禾液肥</div>
    <div class="brand__en">TIAN HE AGRI COMPANY</div>
  </div>

  <div class="holder">
    <div class="holder__en">Daniel Lo</div>
    <div class="holder__zh">陳明達</div>
  </div>

  <ul class="contacts">
    <li>
      <svg viewBox="0 0 16 16"><path fill="#fff" d="M3 1l3 3-1.5 2a9 9 0 0 0 5 5L11 9.5l3 3-2 2.5C6 14.5 1.5 10 1 3z"/></svg>
      886-48-516042
    </li>
    <li>
      <svg viewBox="0 0 16 16"><rect x="2" y="6" width="12" height="8" rx="1" fill="#fff"/><rect x="4" y="1" width="8" height="6" fill="none" stroke="#fff" stroke-width="1.5"/></svg>
      886-48-590714
    </li>
    <li>
      <svg viewBox="0 0 16 16"><rect x="4" y="1" width="8" height="14" rx="1.5" fill="none" stroke="#fff" stroke-width="1.6"/><circle cx="8" cy="12.5" r="1" fill="#fff"/></svg>
      886-912-804-153
    </li>
    <li>
      <svg viewBox="0 0 16 16"><rect x="1" y="3" width="14" height="10" rx="1" fill="#fff"/><path d="M1.5 3.5 8 9l6.5-5.5" fill="none" stroke="var(--leaf-green)" stroke-width="1.4"/></svg>
      daniel58@tianhe-agri.tw
    </li>
  </ul>

  <address class="address" style="font-style:normal">
    <div>No.58, Baoan Rd, Dapu Township, Kexi County , TAIWAN(R.O.C)</div>
    <div class="address__zh">柯溪縣大埔鎮寶安路58號</div>
  </address>
</section>

<section class="card card--back" aria-label="Name card, back">
  <svg class="card__shapes" viewBox="0 0 540 320">
    <defs>
      <linearGradient id="field-tone" x1="0" y1="0" x2="0" y2="1">
        <stop offset="0" stop-color="var(--photo-field-soft)"/>
        <stop offset="1" stop-color="var(--photo-field)"/>
      </linearGradient>
      <linearGradient id="orchard-tone" x1="0" y1="0" x2="0" y2="1">
        <stop offset="0" stop-color="var(--photo-orchard)"/>
        <stop offset="1" stop-color="var(--photo-orchard-soft)"/>
      </linearGradient>
    </defs>
    <path role="img" aria-label="Photo: tractor boom sprayer watering a green field"
          d="M0 0 H140 C260 60 265 250 150 320 H0 Z" fill="url(#field-tone)"/>
    <path d="M140 0 C260 60 265 250 150 320" fill="none" stroke="var(--deep-brown)" stroke-width="3"/>
    <path role="img" aria-label="Photo: orchard sprayer driving between blossoming peach trees"
          d="M540 0 H425 C345 70 345 250 430 320 H540 Z" fill="url(#orchard-tone)"/>
    <path d="M425 0 C345 70 345 250 430 320" fill="none" stroke="var(--deep-brown)" stroke-width="3"/>
  </svg>
  <div class="back-disc"></div>
  <div class="brand brand--back">
    <div class="brand__zh">田禾液肥</div>
    <div class="brand__en">TIAN HE AGRI COMPANY</div>
  </div>
</section>

</body>
</html>
```